Pitch deck for fundraising for a timber drying business

We have the basic content in a powerpoint but need someone to take that and make an attractive and engaging document for a reader who may see hundreds of these a week so visual impact is key.
We are launching a timber drying business in Australia using an exclusive line of kilns not otherwise available in Australia.
Designs should focus on natural tones and connections with forests and timber, probably with a green (colour) focus.

Target Market(s)

investors, wealthyindividuals

Colors

Designer to choose colors to be used in the design.

Requirements
Nice to have
• Design in Canva or similar

```html
<!DOCTYPE html>
<html lang="en">
<head>
<meta charset="utf-8">
<title>Kilnwood Ventures Pitch Deck</title>
<link href="https://fonts.googleapis.com/css2?family=Poppins:wght@300;400;600;700;800&display=swap" rel="stylesheet">
<style>
:root{
  --board:#323c4e;
  --forest:#2d4a1a;
  --leaf:#00b050;
  --moss:#4f7a2a;
  --pale:#e2efda;
  --mist:#eef5ea;
  --grey:#efefef;
  --ink:#3a3a3a;
  --white:#ffffff;
}
*{margin:0;padding:0;box-sizing:border-box}
html,body{width:800px;height:1200px;overflow:hidden;background:var(--board);font-family:'Poppins',sans-serif;color:var(--ink)}
.board{position:relative;width:800px;height:1200px}
.slide{position:absolute;width:342px;height:192px;background:var(--white);box-shadow:8px 10px 22px rgba(0,0,0,.35);overflow:hidden}
.slide::after{content:"";position:absolute;left:0;right:0;bottom:0;height:1.5px;background:var(--leaf)}
.slide-title{position:absolute;left:0;right:0;text-align:center;font-weight:800;color:var(--forest);font-size:13px;line-height:1}
.divider{position:absolute;left:50%;width:26px;margin-left:-13px;height:1px;background:var(--leaf);opacity:.7}
.photo{position:absolute}
.small{font-size:4.6px;line-height:1.35;font-weight:300}
.hl{color:var(--leaf);font-weight:700}
.b{font-weight:700}

/* cover */
.cover .photo{left:12px;top:11px;width:148px;height:170px;background:radial-gradient(circle at 50% 45%,#d8ecb8 0%,#7fbf3f 35%,#3e7a22 70%,#1f3a12 100%)}
.cover .panel{position:absolute;left:166px;top:11px;width:163px;height:170px;background:var(--pale)}
.cover .bar{position:absolute;left:329px;top:11px;width:13px;height:170px;background:var(--leaf)}
.cover h1{position:absolute;left:166px;width:163px;top:64px;text-align:center;font-size:12.5px;font-weight:800;color:var(--forest);line-height:1.25}
.cover .date{position:absolute;left:166px;width:163px;top:110px;text-align:center;font-size:8px;font-weight:400}

/* intro */
.intro .box{position:absolute;left:12px;top:43px;width:318px;height:137px;background:linear-gradient(#f2f2f2 0%,#f2f2f2 60%,#e8ece8 100%)}
.intro .treeline{position:absolute;left:0;right:0;bottom:0;height:55px;background:linear-gradient(rgba(255,255,255,0) 0%,#9fb7a4 45%,#2f5a2c 85%,#1e3d1c 100%)}
.intro .col{position:absolute;top:55px;width:130px}
.intro .col p{margin-bottom:9px}

/* business model */
.model .sub{position:absolute;top:40px;left:30px;right:30px;text-align:center;font-size:5.8px;line-height:1.3}
.model .band{position:absolute;left:0;right:0;top:90px;height:72px;background:linear-gradient(90deg,#3e5c22,#4f6f2e 50%,#3a5a20)}
.model .step{position:absolute;top:64px;width:66px}
.model .step .photo{position:relative;width:66px;height:46px;border:2px solid var(--white)}
.model .step .frame{margin-top:3px;border:.6px dashed rgba(255,255,255,.6);height:26px;text-align:center;color:var(--white)}
.model .step .lbl{font-size:4.8px;font-weight:300;line-height:1.2;padding-top:2px}
.model .step .val{font-size:6.8px;font-weight:700;margin-top:2px}
.model .net{position:absolute;top:172px;left:0;right:0;text-align:center;font-size:9.5px;font-weight:300;color:var(--forest)}

/* market */
.market .head{position:absolute;left:0;right:0;top:0;height:33px;background:var(--mist)}
.market ul{position:absolute;left:15px;top:50px;width:180px;list-style:none}
.market li{position:relative;padding-left:8px;margin-bottom:4px;font-size:4px;line-height:1.3;font-weight:300}
.market li::before{content:"";position:absolute;left:0;top:1.5px;width:2.6px;height:2.6px;border:.7px solid var(--leaf);transform:rotate(45deg)}
.market .frame{position:absolute;left:225px;top:41px;width:100px;height:117px;border:4px solid var(--leaf)}
.market .photo{left:206px;top:60px;width:98px;height:117px;background:linear-gradient(#b3a9a4 0%,#e6b07f 30%,#6c7b76 55%,#2f4a34 80%,#3d4a3a 100%)}

/* post drying */
.post .left{position:absolute;left:0;top:52px;width:138px;height:118px;background:var(--pale)}
.post ul{position:absolute;left:12px;top:62px;width:120px;list-style:none}
.post li{position:relative;padding-left:7px;margin-bottom:4px;font-size:5px;line-height:1.3;font-weight:300}
.post li::before{content:"";position:absolute;left:0;top:1.8px;width:2.6px;height:2.6px;border:.7px solid var(--leaf);transform:rotate(45deg)}
.post .photo{left:141px;top:52px;width:178px;height:118px;background:linear-gradient(135deg,#5a5048 0%,#a69a86 40%,#d8cbb0 60%,#6b665f 100%)}
.post .bar{position:absolute;left:326px;top:52px;width:16px;height:118px;background:var(--leaf)}

/* financials */
.fin .chart{position:absolute;left:10px;top:40px;width:190px;height:86px}
.fin table{position:absolute;left:16px;top:133px;width:178px;border-collapse:collapse;font-size:3.8px}
.fin th{background:var(--forest);color:var(--white);font-weight:600;font-size:4.6px;height:9px}
.fin td{height:9.4px;padding-left:4px;font-weight:700;color:var(--forest)}
.fin tr:nth-child(odd) td{background:var(--pale)}
.fin tr:nth-child(even) td{background:#f4f4f4}
.fin .note{position:absolute;left:210px;top:45px;width:115px;height:134px;background:var(--grey);padding:12px 10px}
.fin .note p{font-size:4.7px;line-height:1.3;font-weight:300;margin-bottom:5px}

/* risk */
.risk .photo{left:241px;top:0;width:101px;height:192px;background:linear-gradient(#8fae3d 0%,#4d7a26 40%,#2e4a1c 75%,#4a3418 100%)}
.risk .slide-title,.risk .divider{right:auto;width:101px}
.risk table{position:absolute;left:22px;top:44px;width:301px;border-collapse:collapse;background:var(--white);box-shadow:0 0 0 2.5px var(--white)}
.risk th{height:13px;color:var(--white);font-size:6px;font-weight:700}
.risk th.r{background:var(--moss);width:105px}
.risk th.m{background:var(--leaf)}
.risk td{font-size:3.6px;line-height:1.3;font-weight:300;padding:2px 5px;height:19.5px;vertical-align:middle;border-bottom:.5px solid #d6e3cc}
.risk td.r{border-right:.5px solid #cfdcc5;font-size:3.8px}
.risk tr:nth-child(odd) td{background:#f4f4f4}
.risk tr:nth-child(even) td{background:var(--pale)}
</style>
</head>
<body>
<main class="board">

  <!-- cover -->
  <section class="slide cover" style="left:41px;top:150px">
    <div class="photo" role="img" aria-label="Looking up into a green forest canopy"></div>
    <div class="panel"></div>
    <div class="bar"></div>
    <h1>KILNWOOD VENTURES<br>PITCH DECK</h1>
    <div class="divider" style="top:102px;left:249px"></div>
    <p class="date">August 11, 2020</p>
  </section>

  <!-- introduction -->
  <section class="slide intro" style="left:417px;top:248px">
    <h2 class="slide-title" style="top:11px">Introduction</h2>
    <div class="divider" style="top:30px"></div>
    <div class="box"></div>
    <div class="treeline" role="img" aria-label="Misty pine treeline"></div>
    <div class="col small" style="left:26px">
      <p>Kilnwood Ventures International (KVI) has secured exclusive access to a superior timber drying technology (AeroDry kilns) that has been in commercial production since 1980.</p>
      <p>KVI will leverage this technology to build a hardwood drying business, initially focused on the stair tread market in Sydney and Brisbane.</p>
      <p>Hardwood stair tread timber has an approximate gross margin of <span class="hl">$XXXX/m3 (XX%)</span>.</p>
      <p>KVI will sell directly to stair tread installers enabling us to retain the bulk of the gross margin as net profit.</p>
    </div>
    <div class="col small" style="left:185px">
      <p>AeroDry kilns are relatively inexpensive <span class="hl">($US79–205K)</span>, modular in design, and return approximately <span class="hl">300%</span> per annum. As a result, KVI will be able to scale without additional equity or debt funding.</p>
      <p>The Australian hardwood industry is worth around <span class="hl">$7bn</span> pa on <span class="hl">700,000m3</span> of sawn timber but <span class="hl">93%</span> of logs are exported. With 10 kilns KVI would dry less than 1% of all sawn timber but turn over <span class="hl">$XXm</span> and nett <span class="hl">$XXm</span> with huge growth potential from value adding exported logs.</p>
      <p>This is not a tech play but a cash cow investment to be held long term. We have a simple business model, using established technology to disrupt a technologically stagnant, but growing industry.</p>
    </div>
  </section>

  <!-- business model -->
  <section class="slide model" style="left:41px;top:387px">
    <h2 class="slide-title" style="top:11px">Business Model</h2>
    <div class="divider" style="top:30px"></div>
    <p class="sub">We are using established technology to disrupt the existing timber supply chain with a simple <span class="b">4 step</span> business model</p>
    <div class="band" role="img" aria-label="Dark forest backdrop"></div>
    <div class="step" style="left:19px">
      <div class="photo" role="img" aria-label="Stacked sawn timber boards" style="background:linear-gradient(135deg,#9a6a4a,#5e3a24)"></div>
      <div class="frame"><div class="lbl">Buy cut timber<br>from sawmills</div><div class="val">$XXX m3</div></div>
    </div>
    <div class="step" style="left:98px">
      <div class="photo" role="img" aria-label="Timber stacked inside a drying kiln" style="background:linear-gradient(90deg,#d9d2c6,#b09170 60%,#7a5a3c)"></div>
      <div class="frame"><div class="lbl">Dry it in our<br>kilns</div><div class="val">$XXXm3</div></div>
    </div>
    <div class="step" style="left:176px">
      <div class="photo" role="img" aria-label="Timber dressing machine in a workshop" style="background:linear-gradient(135deg,#cdd3d8,#6d7680 55%,#3b3128)"></div>
      <div class="frame"><div class="lbl">Dress and<br>deliver</div><div class="val">$XXX m3</div></div>
    </div>
    <div class="step" style="left:257px">
      <div class="photo" role="img" aria-label="Finished hardwood stair tread" style="background:radial-gradient(ellipse at center,#6e3a22 0%,#8a4a2a 25%,var(--pale) 45%)"></div>
      <div class="frame"><div class="lbl">Sell dried stair<br>treads to installers</div><div class="val">$XXXm3</div></div>
    </div>
    <p class="net">~ <span class="hl">$XXXm3</span> Net profit</p>
  </section>

  <!-- market overview -->
  <section class="slide market" style="left:417px;top:485px">
    <div class="head"></div>
    <h2 class="slide-title" style="top:11px">Market Overview</h2>
    <div class="divider" style="top:31px"></div>
    <ul>
      <li>The total value of the Australian timber market is <span class="b">$23.9bn*</span> with hardwood accounting for over <span class="b">$7bn</span> and softwood the balance. The Australian hardwood market has been growing strongly, posting 10% growth in volume of logs harvested and a 13% increase in price in 2017 despite a 5% fall in housing construction.</li>
      <li>The hardwood industry however is massively under developed with <span class="b">93%*</span> of all plantation hardwood logs being exported – with no value adding.</li>
      <li>The total volume of sawn hardwood timber in 2018 was 700,000m3. With just 10 kilns we would dry less than 0.800m3 pa, gross <span class="b">$30.6m</span> in revenue and net <span class="b">$18.5m</span> with significant opportunity to expand.</li>
      <li>In NSW logs are sourced through either Regional Forest Authority (Owen knows and has worked with the Chair previously) on either a quota or spot price basis or through the logging of private forests. KVI will commence by sourcing timber from private forests as there are numerous landholders and contract loggers to ensure timber supply and mitigate sourcing risk.</li>
      <li>To quantify the direct addressable market KVI conducted extensive market research, contacting 98 stair installers, joineries and furniture manufacturers in addition to wholesalers. Stair installers pay between $XXX and $XXXXm3 with an average of just over $XX00m3 whereas wholesalers buy at around <span class="b">$XX00m3</span>.</li>
      <li>Include Ross's timber data on stair tread market</li>
    </ul>
    <div class="frame"></div>
    <div class="photo" role="img" aria-label="Pine trees and mountains at sunset"></div>
  </section>

  <!-- post drying -->
  <section class="slide post" style="left:41px;top:624px">
    <h2 class="slide-title" style="top:11px">Post Drying Process</h2>
    <div class="divider" style="top:30px"></div>
    <div class="left"></div>
    <ul>
      <li>Dried stair treads are either delivered skip dressed or sized and finished with volumes being around 50:50 of each. We will commence by offering a skip dressed product as it is the simplest to produce.</li>
      <li>Skip dressing involves running the dried timber through a thicknesser or moulder to roughly level two sides of timber and expose the grain. This allows the quality of the timber grade (Select, Standard or feature) to be assessed.</li>
      <li>Once dressed, the timber is palletised ready for delivery to the client.</li>
    </ul>
    <div class="photo" role="img" aria-label="Boards feeding into a thicknesser machine"></div>
    <div class="bar"></div>
  </section>

  <!-- financials -->
  <section class="slide fin" style="left:417px;top:722px">
    <h2 class="slide-title" style="top:11px">Financials</h2>
    <div class="divider" style="top:30px"></div>
    <svg class="chart" viewBox="0 0 190 86" aria-label="Revenue and EBITDA by year">
      <g font-family="Poppins, sans-serif" font-size="3" fill="#555" text-anchor="end">
        <text x="22" y="5">$30,000,000</text>
        <text x="22" y="17">$25,000,000</text>
        <text x="22" y="29">$20,000,000</text>
        <text x="22" y="41">$15,000,000</text>
        <text x="22" y="53">$10,000,000</text>
        <text x="22" y="65">$5,000,000</text>
        <text x="22" y="77">$0</text>
      </g>
      <g stroke="#e3e3e3" stroke-width=".4">
        <line x1="25" y1="4" x2="138" y2="4"/><line x1="25" y1="16" x2="138" y2="16"/>
        <line x1="25" y1="28" x2="138" y2="28"/><line x1="25" y1="40" x2="138" y2="40"/>
        <line x1="25" y1="52" x2="138" y2="52"/><line x1="25" y1="64" x2="138" y2="64"/>
        <line x1="25" y1="76" x2="138" y2="76"/>
      </g>
      <rect x="35" y="69" width="9" height="7" fill="#a8d08d"/>
      <rect x="46" y="72" width="9" height="4" fill="#00b050"/>
      <rect x="75" y="34" width="9" height="42" fill="#a8d08d"/>
      <rect x="86" y="56" width="9" height="20" fill="#00b050"/>
      <rect x="115" y="12" width="9" height="64" fill="#a8d08d"/>
      <rect x="126" y="39" width="9" height="37" fill="#00b050"/>
      <g font-family="Poppins, sans-serif" font-size="4" fill="#555" text-anchor="middle">
        <text x="45" y="83">Year 1</text><text x="85" y="83">Year 2</text><text x="125" y="83">Year 3</text>
      </g>
      <rect x="143" y="36" width="2.5" height="2.5" fill="#a8d08d"/>
      <text x="147" y="38.6" font-family="Poppins, sans-serif" font-size="3.4" fill="#555">Revenue</text>
      <rect x="143" y="44" width="2.5" height="2.5" fill="#00b050"/>
      <text x="147" y="46.6" font-family="Poppins, sans-serif" font-size="3.4" fill="#555">EBITDA</text>
    </svg>
    <table>
      <tr><th style="width:70px"></th><th>Year 1</th><th>Year 2</th><th>Year 3</th></tr>
      <tr><td>EBITDA</td><td></td><td></td><td></td></tr>
      <tr><td>Cumulative cash</td><td></td><td></td><td></td></tr>
      <tr><td>No. kilns</td><td></td><td></td><td></td></tr>
      <tr><td>Monthly Recurring Profit</td><td></td><td></td><td></td></tr>
    </table>
    <div class="note">
      <p>Kilnwood Ventures will offer investors high levels of cash returns with the business netting around <span class="hl">$XXK</span> pm with just the AeroDry Plus and almost $XXK pm with a Plus and a Turbo in month 7.</p>
      <p>From there we will ramp up production capacity in accordance with sales and AeroDry production capacity.</p>
      <p>We view KVI as a long term hold, paying out <span class="hl">80%+</span> of net profit where there aren't opportunities to grow the business.</p>
      <p>By the time we have 10 total kilns (end of year 3) we expect to be distributing a total of approximately <span class="hl">$XX</span> per month and retaining <span class="hl">$XXK</span> pm.</p>
    </div>
  </section>

  <!-- risk -->
  <section class="slide risk" style="left:41px;top:861px">
    <div class="photo" role="img" aria-label="Sunlit forest trail"></div>
    <h2 class="slide-title" style="top:11px;left:120px">Risk</h2>
    <div class="divider" style="top:30px;left:170px"></div>
    <table>
      <tr><th class="r">Risk</th><th class="m">Mitigation</th></tr>
      <tr><td class="r">Disruption to log supply</td><td>Our regional base is central to the hardwood timber forests of the north coast, allowing KVI to economically draw timber from a wider geographic area reducing the potential for localised issues such as weather or fires to impact supply.</td></tr>
      <tr><td class="r">Unable to obtain boards from sawmills</td><td>Diversify supply of boards, contract with state and private forests for own supply of logs and use contract sawmilling. Phase 3 develop own sawmilling capacity.</td></tr>
      <tr><td class="r">Timber boards not to specification</td><td>Inspect and test delivered timber pre-drying to allow rejection of out of specification boards. Inspect post-drying boards to ensure they meet specification. Consider independent testing as part of outbound QA process.</td></tr>
      <tr><td class="r">Kiln doesn't perform to expectations</td><td>Warranty and product support for a fault. If operation of machine does not achieve expected levels of output increase number of machines or air-dry timber before placement in kiln to reduce kiln times.</td></tr>
      <tr><td class="r">Ability to supply required species timber</td><td>We will initially only dry loads of the most commonly used timber – blackbutt. As capacity and confidence in quality improve we will start to broaden the range of species we dry, this will also help mitigate any risks around supply of timber.</td></tr>
      <tr><td class="r">Copycat competitor</td><td>Our exclusive agreement for the supply of AeroDry equipment excludes direct competition in the short term but there are alternative kilns but with lesser performance. Phase 2 of the strategic plan is focussed on developing a highly connected and integrated sales channel with the market in order to create a barrier to entry.</td></tr>
    </table>
  </section>

</main>
</body>
</html>
```